DEADLINE 4 JAN 2015 - Drama Movie POSTER

Title of movie " KORAL " - in English SUNSET, Koral is a Sanskrit language, we expect the font to be a little towards that influence ( ethnic )

STORY:
This movie is about one girl's life survival, played by actress ( MIRA HALVORSEN ) fighting her life out of leukemia, deceived in relationship, denying love, searching for her birth father and later kidnapped but saved.

GENRE:
Its a drama with twist of thriller in the end.

COUNTRIES INVOLVED:
Phuket islands in Thailand and Bali and city scenes in Jakarta, Singapore and Istanbul.

We upload photos of actors involved, and we CAN have them on the poster, you can be creative but yet keep it elegant and sophisticated, the movie is for an upmarket. So we dont want too much color. Sunset color mixed with dark or black is nice.

Look forward to see you creative design! Thanks so much!

ACTORS NAME:
- Rudy Pelangi
- Kit B Mayhew
- Tobias Wen
- K Trax
- Hendra Sulut
- Mateo Brunvelli
- Mira Halvorsen
- Sari Lynne
- Ayu Kemalasari
- Ruqaya
- Felix Moro
- Yos Latuheru
- Faustino Medeira

TITLE OF MOVIE:
KORAL - " we love, we cry, we fall but we survive "

If you need sample of promotional trailer, please request with your email address.

Please Check our Brief as we have edited and add some more information needed.Many thanks and look forward to your arts.Warm Regards,KorvoStage Pictures Added Sunday, December 21, 2014

Investors, Young Adults and Adults Crowds

Movie

• Ethnic

• Movie title and Quotes : " we love, we cry, we fall but we survive "
• ( with or without logo ) Production House:
• KorvoStage Pictures in collaboration with Glimmerax.Inc
• Director's name:
• Budi Sastro & Teguh Rambukasih
• Actor Names in order:
• Rudy Pelangi, Ktrax, Sari Lynne, Hendra Sulut, Tobias Wen, Ayu Kemalasari, Felix Moro, Kit B Mayhew, Ruqaya, Mateo Brunvelli, Yos Latuheru, Mira Halvorsen, Faustino Medeira
• Poster influences: Fallow Ridge
• If you want to use the same idea, you can use a silhouette of a girl
• from one of mira halvorsen's picture WITHOUT exposing her face

```html
<!DOCTYPE html>
<html lang="en">
<head>
<meta charset="utf-8">
<title>KORAL — Poster</title>
<link href="https://fonts.googleapis.com/css2?family=Permanent+Marker&family=Dancing+Script:wght@600&family=Barlow+Condensed:wght@400&display=swap" rel="stylesheet">
<style>
  :root {
    --page: #ffffff;
    --poster: #000000;
    --sun-deep: #2a120c;
    --sun-mid: #e8561f;
    --sun-gold: #f7b81e;
    --ember: #8c1c12;
    --portrait-light: #c9c9c9;
    --portrait-dark: #3a3a3a;
  }
  * { margin: 0; padding: 0; box-sizing: border-box; }
  html, body { width: 1200px; height: 900px; overflow: hidden; background: var(--page); }
  .canvas { position: relative; width: 1200px; height: 900px; background: var(--page); }
  .poster { position: absolute; left: 297px; top: 0; width: 606px; height: 900px; background: var(--poster); }
  .artwork { position: absolute; left: 0; top: 0; }
  .title {
    position: absolute; left: 0; width: 606px; top: 428px; text-align: center;
    font-family: "Permanent Marker", cursive; font-size: 128px; line-height: 1;
    letter-spacing: 4px;
    background: linear-gradient(180deg, var(--sun-gold) 10%, var(--sun-mid) 90%);
    -webkit-background-clip: text; background-clip: text; color: transparent;
  }
  .tagline {
    position: absolute; left: 0; width: 606px; top: 590px; text-align: center;
    font-family: "Dancing Script", cursive; font-weight: 600; font-size: 19px;
    color: var(--ember); letter-spacing: 0.5px;
  }
  .cast {
    position: absolute; top: 698px; width: 180px; text-align: center; list-style: none;
    font-family: "Barlow Condensed", sans-serif; font-size: 13px; line-height: 19px;
    letter-spacing: 0.8px; color: var(--ember);
  }
  .cast--left { left: 27px; }
  .cast--middle { left: 211px; }
  .cast--right { left: 405px; }
  .studio {
    position: absolute; left: 98px; top: 828px; width: 40px; text-align: center;
  }
  .studio-mark {
    display: block; width: 20px; height: 20px; margin: 0 auto 3px;
    border-radius: 50%; background: var(--ember);
  }
  .studio-name {
    display: block; font-family: "Barlow Condensed", sans-serif; font-size: 5px;
    letter-spacing: 0.4px; color: var(--ember); white-space: nowrap;
    margin-left: -10px; width: 60px;
  }
  .credits {
    position: absolute; left: 160px; top: 846px; width: 380px;
    font-family: "Barlow Condensed", sans-serif; font-size: 9px; line-height: 11px;
    letter-spacing: 0.6px; color: var(--ember);
  }
</style>
</head>
<body>
<div class="canvas">
  <main class="poster">
    <svg class="artwork" width="606" height="430" viewBox="0 0 606 430">
      <defs>
        <linearGradient id="sunBar" x1="0" y1="0" x2="0" y2="1">
          <stop offset="0" stop-color="var(--sun-deep)"/>
          <stop offset="0.55" stop-color="var(--sun-mid)"/>
          <stop offset="1" stop-color="var(--sun-gold)"/>
        </linearGradient>
        <linearGradient id="portraitTone" x1="0" y1="0" x2="1" y2="1">
          <stop offset="0" stop-color="var(--portrait-dark)"/>
          <stop offset="0.5" stop-color="var(--portrait-light)"/>
          <stop offset="1" stop-color="var(--portrait-dark)"/>
        </linearGradient>
      </defs>
      <path class="portrait" role="img" aria-label="Black and white portrait of the lead actress, framed in a rounded cut-out"
            d="M168 240 C168 150 235 68 328 66 C420 68 488 150 488 240 C488 330 415 395 328 395 C241 395 168 330 168 240 Z"
            fill="url(#portraitTone)"/>
      <rect class="bar-cut" x="301" y="60" width="8" height="340" fill="var(--poster)"/>
      <rect class="bar-cut" x="333" y="60" width="8" height="340" fill="var(--poster)"/>
      <rect class="sun-bar" x="264" y="0" width="29" height="417" fill="url(#sunBar)"/>
    </svg>

    <h1 class="title">KORAL</h1>
    <p class="tagline">we love, we cry, we fall but we survive.</p>

    <ul class="cast cast--left">
      <li>RUDY PELANGI</li>
      <li>TOBIAS WEN</li>
      <li>KIT B MAYHEW</li>
      <li>MIRA HALVORSEN</li>
    </ul>
    <ul class="cast cast--middle">
      <li>KTRAX</li>
      <li>SARI LYNNE</li>
      <li>AYU KEMALASARI</li>
      <li>MATEO BRUNVELLI</li>
      <li>RUQAYA</li>
    </ul>
    <ul class="cast cast--right">
      <li>HENDRA SULUT</li>
      <li>FELIX MORO</li>
      <li>YOS LATUHERU</li>
      <li>FAUSTINO MEDEIRA</li>
    </ul>

    <div class="studio">
      <span class="studio-mark"></span>
      <span class="studio-name">KORVOSTAGE PICTURES</span>
    </div>
    <p class="credits">DIRECTED BY BUDI SASTRO, A STORY BY MIRA HALVORSEN IN COLLABORATION WITH<br>GLIMMERAX INC AND DIRECTOR OF PHOTOGRAPHY TEGUH RAMBUKASIH</p>
  </main>
</div>
</body>
</html>
```